Health and Wellness Company Needs Brochure to Describe New Exercise Class Offering

We need a brochure to help clients better understand our new service offering. We are a Portland, OR based health and wellness company called 'stride haven studio'. We provide instruction in group exercise classes designed to reduce pain and improve movement. Similar to physical therapy but with the teaching environment similar to a yoga studio.

Please see attached word document that outlines the sections that should be included in the brochure.

We would like to see the color orange throughout the brochure as that color reflects vitality and energy. Our logo should be included in the design. Our slogan is "Feel Better. Move Better. Live Better." Go to our website www.stridehavenstudio.example for more information.

Target Market(s)

Exercise conscious, recreational athletes who are proactive about their health and well-being and looking for an alternative to physical therapy.

Industry/Entity Type

Health And Wellness

Font styles to use
Sans Serif

Requirements
Must have
• Logo placed strategically throughout the brochure.
• A trifold brochure.
Should not have
• I'd like to avoid the standard 3 panel design. Instead I'd like to see the design spread out over the page with 3 sections arbitrarily created by the designer that doesn't follow the fold pattern of the trifold brochure.

```html
<!DOCTYPE html>
<html lang="en">
<head>
<meta charset="utf-8">
<title>Stride Haven Studio – Brochure Inside Spread</title>
<link rel="stylesheet" href="https://fonts.googleapis.com/css2?family=Mulish:wght@300;400&display=swap">
<style>
  :root {
    --ink: #0b0b0c;
    --orange: #f39a1e;
    --body-text: #d4d4d4;
    --page: #ffffff;
  }
  * { margin: 0; padding: 0; box-sizing: border-box; }
  html, body { width: 1200px; height: 800px; overflow: hidden; background: var(--page); }
  body { font-family: "Mulish", "Helvetica Neue", Arial, sans-serif; }

  .spread { position: relative; width: 1200px; height: 800px; overflow: hidden; background: var(--ink); }
  .spread-art { position: absolute; inset: 0; width: 1200px; height: 800px; }

  .section { position: absolute; color: var(--body-text); }
  .section-title {
    font-weight: 300;
    color: var(--orange);
    font-size: 29px;
    line-height: 1.12;
    letter-spacing: 0.3px;
    margin-bottom: 16px;
  }
  .section-title .title-line2 { display: block; font-size: 22px; }
  .section p {
    font-size: 12.5px;
    font-weight: 300;
    line-height: 1.65;
    margin-bottom: 14px;
  }
  .section .callout {
    font-size: 17px;
    line-height: 1.3;
    font-style: italic;
    color: var(--orange);
    font-weight: 300;
    margin-top: 4px;
  }

  .section--posture  { left: 52px;  top: 430px; width: 310px; }
  .section--cause    { left: 448px; top: 408px; width: 315px; }
  .section--approach { left: 845px; top: 352px; width: 325px; }
</style>
</head>
<body>
<main class="spread">
  <svg class="spread-art" viewBox="0 0 1200 800" xmlns="http://www.w3.org/2000/svg">
    <defs>
      <linearGradient id="photo-posture" x1="0" y1="0" x2="1" y2="1">
        <stop offset="0" stop-color="#efe6de"/>
        <stop offset="0.45" stop-color="#b98a6c"/>
        <stop offset="1" stop-color="#f3eee9"/>
      </linearGradient>
      <linearGradient id="photo-studio" x1="0" y1="0" x2="1" y2="1">
        <stop offset="0" stop-color="#e9c9a6"/>
        <stop offset="0.5" stop-color="#8f8a86"/>
        <stop offset="1" stop-color="#f2dcc4"/>
      </linearGradient>
      <linearGradient id="photo-field" x1="0" y1="0" x2="0" y2="1">
        <stop offset="0" stop-color="#f7f6f0"/>
        <stop offset="0.45" stop-color="#c9d1a4"/>
        <stop offset="1" stop-color="#5f7a2a"/>
      </linearGradient>
      <linearGradient id="panel-shade" x1="0" y1="0" x2="0" y2="1">
        <stop offset="0" stop-color="#141416"/>
        <stop offset="1" stop-color="#050506"/>
      </linearGradient>
    </defs>

    <rect x="0" y="0" width="400" height="420" fill="url(#photo-posture)" role="img" aria-label="Photo: woman checking her posture in a mirror"/>
    <rect x="400" y="0" width="400" height="400" fill="url(#photo-studio)" role="img" aria-label="Photo: group exercise class in a bright studio"/>
    <rect x="800" y="0" width="400" height="360" fill="url(#photo-field)" role="img" aria-label="Photo: woman holding a yoga pose on a grassy field"/>

    <path class="dark-panel" fill="url(#panel-shade)"
      d="M0 405 Q200 385 400 392 Q600 372 800 340 Q1000 300 1200 268 L1200 800 L0 800 Z"/>
    <path class="orange-edge" fill="none" stroke="var(--orange)" stroke-width="6"
      d="M0 405 Q200 385 400 392 Q600 372 800 340 Q1000 300 1200 268"/>
    <path class="orange-rule" fill="none" stroke="var(--orange)" stroke-width="2"
      d="M0 778 Q200 770 400 762 Q600 764 800 760 Q1000 758 1200 752"/>
  </svg>

  <section class="section section--posture">
    <h2 class="section-title">What Does Your <span class="title-line2">Posture Say About You?</span></h2>
    <p>The easiest way to identify muscle compensation is to look for misalignments in your body. Place your hands on your waist line. Is one hip higher than the other? Does one foot turn out more? Is one shoulder higher than the other?</p>
    <p>If you answered YES to any of these questions, your pain is likely the result of muscle compensation and can benefit from the stride haven method!</p>
  </section>

  <section class="section section--cause">
    <h2 class="section-title">The Real Cause <span class="title-line2">of Your Pain</span></h2>
    <p>Most muscle and joint pain is the result of deactivated muscles losing their ability to perform their designed functions. To compensate for the weakness, the remaining stronger muscles of the body take on additional roles they were not meant to play. This gradual process leads to tension in your overworked muscles, the misalignment of your body, and accelerated wear and tear of your joints.</p>
    <p class="callout">Fortunately, this process<br>is reversible.</p>
  </section>

  <section class="section section--approach">
    <h2 class="section-title">How Our <span class="title-line2">Approach Works</span></h2>
    <p>We believe that everything in the body is interconnected, with seemingly unrelated problems in one area influencing other areas. That's why regardless of where you experience symptoms, whether it's in your knee or low back, it's our philosophy to exercise the body as one whole system rather than as independent parts.</p>
    <p>Certified instructors lead small group exercise classes designed by physical therapists. By specifically targeting and exercising the deactivated muscles, stride haven studio helps you reduce compensation, restore the alignment of your body, and eliminate pain. You get the same exercise instruction you'd receive in physical therapy but at a fraction of the cost.</p>
  </section>
</main>
</body>
</html>
```